Allied Health team of Physiotherapists & Occupational Therapists seek a business card design

We have our new logo, we now need our new business cards and stationary. Blossom: Lymphoedema & Women's Clinic is seeking a generic card design to represent our whole team and individual cards for each therapist that incorporates our new logo to communicate our holistic approach that is calming, nuturing, supportive and welcoming.
Our Physiotherapists and Occupational Therapists assess, treat and provide education for people who are at risk of or who have lymphoedema. This is often as a result of treatment for cancer. We provide pre-operative and post-operative management and cancer rehabilitation in our Pilates studio. Our team also consists of Physiotherapists who have a strong interest in pelvic floor and continence management for both men and women.

Target Market(s)

Mainly women health conscious

Industry/Entity Type

Allied Health: Physiotherapy / Occupational Therapy

Contact Information for Business Card

Address: 14 Calloway Ave Bayhaven 3921 Phone: 84317560 fax: 8431 7564 Email: info@blossomcarepartners.com.au Website: blossomcarepartners.com.au Facebook address: facebook.com/BlossomLymphoedemaAndWomensCareCentre. Room to write appointments. Individual cards need to have name, office email and individual email and professional details

Requirements
Must have
• Logo as per uploaded documents

```html
<!DOCTYPE html>
<html lang="en">
<head>
<meta charset="utf-8">
<title>Blossom Business Cards</title>
<link href="https://fonts.googleapis.com/css2?family=Allura&family=Merriweather:ital,wght@0,400;0,700;1,400&display=swap" rel="stylesheet">
<style>
  :root {
    --peach: #f8ae80;
    --peach-text: #f2a06e;
    --peach-soft: #fde9dc;
    --sage: #b7c6b6;
    --ink: #555555;
    --white: #ffffff;
    --backdrop: #e9e6e3;
  }
  * { box-sizing: border-box; margin: 0; padding: 0; }
  html, body { width: 1200px; height: 895px; overflow: hidden; }
  body {
    background: var(--backdrop);
    font-family: "Merriweather", Georgia, serif;
    color: var(--ink);
    display: flex; flex-direction: column; align-items: center; justify-content: center;
    gap: 44px;
  }
  .card {
    width: 630px; height: 360px;
    background: var(--white);
    position: relative;
    box-shadow: 0 6px 18px rgba(0,0,0,.15);
    overflow: hidden;
  }

  /* Front */
  .card--front { display: flex; }
  .front__details {
    width: 56%; padding: 46px 20px 0 44px;
    display: flex; flex-direction: column; align-items: center; text-align: center;
  }
  .person-name {
    font-family: "Allura", cursive; color: var(--peach-text);
    font-size: 58px; line-height: 1; font-weight: 400;
  }
  .credentials { font-size: 10px; font-style: italic; margin-top: 8px; line-height: 1.55; white-space: nowrap; }
  .role { font-size: 12.5px; margin-top: 4px; }
  .divider { width: 140px; height: 1.5px; background: var(--peach-text); margin: 14px 0 16px; }
  .contact { list-style: none; font-size: 13px; line-height: 1.75; text-align: left; align-self: flex-start; margin-left: 20px; }
  .contact li { display: flex; align-items: center; gap: 10px; white-space: nowrap; }
  .contact svg { width: 14px; height: 14px; flex: none; }
  .front__brand {
    width: 44%; display: flex; align-items: center; justify-content: center; padding-right: 20px;
  }
  .brand {
    display: flex; flex-direction: column; align-items: center; gap: 12px; text-align: center;
  }
  .brand__dot { width: 96px; height: 96px; border-radius: 50%; border: 2px solid var(--peach-soft); }
  .brand__name { font-size: 30px; color: var(--peach-text); font-weight: 400; }
  .brand__tag { font-size: 10px; letter-spacing: 1.5px; color: var(--peach-text); white-space: nowrap; }

  /* Back */
  .card--back { display: flex; }
  .back__panel {
    width: 33%; background: var(--peach);
    display: flex; align-items: center; justify-content: center;
  }
  .back__panel .brand__name, .back__panel .brand__tag { color: var(--white); }
  .back__panel .brand__dot { border-color: rgba(255,255,255,.6); }
  .back__panel .brand__tag { font-size: 7.5px; letter-spacing: 1px; }
  .back__main { width: 67%; position: relative; padding: 40px 34px 0 40px; }
  .leaf-wash {
    position: absolute; right: 40px; top: 40px; width: 220px; height: 200px;
    background: radial-gradient(ellipse at center, var(--peach-soft) 0%, rgba(253,233,220,0) 70%);
  }
  .appt-title { font-size: 27px; font-weight: 700; color: var(--peach-text); position: relative; }
  .appt-fields { list-style: none; margin-top: 30px; position: relative; }
  .appt-fields li { display: flex; align-items: flex-end; gap: 8px; font-size: 13px; height: 34px; }
  .appt-fields .line { flex: 1; border-bottom: 1px dashed #777; margin-bottom: 4px; }
  .sage-rule { height: 2px; background: var(--sage); margin: 22px -34px 0 0; position: relative; }
  .location { list-style: none; font-size: 13px; margin-top: 10px; position: relative; }
  .location li { display: flex; align-items: center; gap: 10px; height: 30px; white-space: nowrap; }
  .location li + li { border-top: 2px solid var(--sage); }
  .location svg { width: 15px; height: 15px; flex: none; }
</style>
</head>
<body>

<section class="card card--front">
  <div class="front__details">
    <h1 class="person-name">Harriet Lowe</h1>
    <p class="credentials">B. Physio<br>Post Grad Certif. Continence &amp; Pelvic Floor Rehabilitation</p>
    <p class="role">Physiotherapist Pelvic Health</p>
    <div class="divider"></div>
    <ul class="contact">
      <li><svg viewBox="0 0 16 16"><path fill="#f2a06e" d="M4 1l2.5 3-1.5 2c1 2 3 4 5 5l2-1.5 3 2.5-1.5 2.5C7 14 2 9 1.5 2.5z"/></svg>84317560 Phone</li>
      <li><svg viewBox="0 0 16 16"><rect x="2" y="5" width="12" height="8" rx="1" fill="#f2a06e"/><rect x="4" y="2" width="8" height="4" fill="#f2a06e"/></svg>8431 7564 Fax</li>
      <li><svg viewBox="0 0 16 16"><rect x="1" y="3" width="14" height="10" rx="1" fill="#f2a06e"/><path d="M1.5 3.5L8 9l6.5-5.5" stroke="#fff" fill="none" stroke-width="1.3"/></svg>harriet@blossomcarepartners.com.au</li>
      <li><svg viewBox="0 0 16 16"><circle cx="8" cy="8" r="6.5" fill="#f2a06e"/><path d="M1.5 8h13M8 1.5c-3 3-3 10 0 13M8 1.5c3 3 3 10 0 13" stroke="#fff" fill="none" stroke-width="1"/></svg>blossomcarepartners.com.au</li>
    </ul>
  </div>
  <div class="front__brand">
    <div class="brand">
      <div class="brand__dot"></div>
      <p class="brand__name">Blossom</p>
      <p class="brand__tag">LYMPHOEDEMA &amp; WOMEN'S CARE CENTRE</p>
    </div>
  </div>
</section>

<section class="card card--back">
  <div class="back__panel">
    <div class="brand">
      <div class="brand__dot"></div>
      <p class="brand__name">Blossom</p>
      <p class="brand__tag">LYMPHOEDEMA &amp; WOMEN'S CARE CENTRE</p>
    </div>
  </div>
  <div class="back__main">
    <div class="leaf-wash" role="img" aria-label="Faint leaf sprig decoration"></div>
    <h2 class="appt-title">Next Appointment</h2>
    <ul class="appt-fields">
      <li>Name: <span class="line"></span></li>
      <li>Date: <span class="line"></span></li>
      <li>Time: <span class="line"></span></li>
    </ul>
    <div class="sage-rule"></div>
    <ul class="location">
      <li><svg viewBox="0 0 16 16"><path fill="#f2a06e" d="M8 1a5 5 0 00-5 5c0 4 5 9 5 9s5-5 5-9a5 5 0 00-5-5z"/><circle cx="8" cy="6" r="2" fill="#fff"/></svg>14 Calloway Ave, Bayhaven 3921</li>
      <li><svg viewBox="0 0 16 16"><circle cx="8" cy="8" r="7" fill="#f2a06e"/></svg>/BlossomLymphoedemaAndWomensCareCentre</li>
    </ul>
  </div>
</section>

</body>
</html>
```